Need a website for our company

We need a website for our company to showcase all our work for customers to see.
We do all phases of home improvement:
Dormers/Extensions
Basement Remodel
Masonry/Concrete/Pavers/Asphalt
Cultured Stone Veneer
Kitchens
Bathrooms
Pool designs
Outdoor Bathroom
Outdoor Kitchens
Tile work
For reference, something similar to this website: https://brightoakrenovations.example/
Target Market(s)
We are trying to target homeowners.
Coding
Number of Pages Required
Look and feel

```html
<!DOCTYPE html>
<html lang="en">
<head>
<meta charset="utf-8">
<title>Halden &amp; Sons Construction Inc</title>
<link href="https://fonts.googleapis.com/css2?family=Exo+2:wght@400;600;700;800&display=swap" rel="stylesheet">
<style>
:root{
  --page:#2b2a33;
  --topbar:#26252c;
  --header:#3a3946;
  --nav:#f4f4f4;
  --accent:#f5c400;
  --text:#ffffff;
  --muted:#8f8e98;
  --dark-text:#2b2a33;
  --line:#45444f;
  --icon:#a9a8b0;
}
*{box-sizing:border-box;margin:0;padding:0}
html,body{width:1200px;height:590px;overflow:hidden}
body{background:var(--page);font-family:"Exo 2",sans-serif;color:var(--text);position:relative}

.topbar{position:absolute;top:0;left:0;width:1200px;height:10px;background:var(--topbar);border-bottom:1px solid var(--line)}
.topbar .address{position:absolute;left:317px;top:1px;font-size:5.5px;line-height:7px;color:var(--muted);display:flex;align-items:center;gap:3px;letter-spacing:.1px}
.topbar .social{position:absolute;left:834px;top:0;display:flex;gap:1px}
.topbar .social span{width:14px;height:9px;background:var(--header);display:flex;align-items:center;justify-content:center}

.header{position:absolute;top:10px;left:0;width:1200px;height:65px;background:var(--header)}
.brand{position:absolute;left:323px;top:10px;display:flex;align-items:flex-end;gap:5px}
.brand-mark{width:34px;height:34px;border:3px solid var(--text);display:block}
.brand-name{font-weight:800;font-size:7.6px;letter-spacing:.35px;color:var(--text);line-height:8px;margin-bottom:-4px}
.contact{position:absolute;top:22px;display:flex;gap:6px;align-items:flex-start}
.contact.hotline{left:744px}
.contact.hours{left:814px;padding-left:11px;border-left:1px solid #55546a;height:22px}
.contact b{display:block;font-size:7px;font-weight:700;line-height:9px}
.contact small{display:block;font-size:6px;color:var(--muted);line-height:9px}

.nav{position:absolute;top:75px;left:0;width:1200px;height:31px;background:var(--nav)}
.nav ul{list-style:none;position:absolute;left:315px;top:12px;height:14px;font-size:6.8px;font-weight:700;letter-spacing:.6px;color:var(--dark-text);line-height:8px}
.nav li{position:absolute;top:0;white-space:nowrap}
.nav li.current{border-bottom:1px solid var(--dark-text);padding-bottom:5px}
.nav .sep{position:absolute;top:1px;width:1px;height:6px;background:var(--dark-text)}

.service{position:absolute}
.service h2{font-size:9.4px;font-weight:700;white-space:nowrap;line-height:11px;letter-spacing:.1px}
.service h2::after{content:"";display:block;width:20px;height:2px;background:var(--accent);margin-top:4px}
.service .photo{position:absolute;left:0}

.footer{position:absolute;top:568px;left:0;width:1200px;height:22px;border-top:1px solid var(--line)}
.footer p{position:absolute;left:315px;top:8px;font-size:5.5px;line-height:7px}
.footer .social{position:absolute;left:792px;top:0;display:flex}
.footer .social span{width:25.5px;height:22px;border-left:1px solid var(--line);display:flex;align-items:center;justify-content:center}
.footer .social span:last-child{border-right:1px solid var(--line)}
.to-top{position:absolute;left:1187px;top:558px;width:14px;height:14px;border-radius:50%;background:var(--accent);display:flex;align-items:center;justify-content:center}
</style>
</head>
<body>
<div class="topbar">
  <div class="address">
    <svg width="5" height="7" viewBox="0 0 10 14"><path d="M5 0a5 5 0 0 1 5 5c0 4-5 9-5 9S0 9 0 5a5 5 0 0 1 5-5z" fill="#f5c400"/><circle cx="5" cy="5" r="2" fill="#26252c"/></svg>
    48 LINDEN AVENUE, FAIRHAVEN, NEW YORK 11920
  </div>
  <div class="social">
    <span><svg width="7" height="5" viewBox="0 0 14 10"><rect width="14" height="10" fill="#f5c400"/><path d="M0 0l7 6 7-6" stroke="#3a3946" fill="none"/></svg></span>
    <span><svg width="6" height="6" viewBox="0 0 12 12"><path d="M3 1l3 1 .5 3-1.5 1c.7 1.6 1.6 2.5 3 3l1-1.5 3 .5 .5 3-2 1C5 11 1 7 1 3z" fill="#f5c400"/></svg></span>
    <span><svg width="5" height="7" viewBox="0 0 10 14"><path d="M5 0a5 5 0 0 1 5 5c0 4-5 9-5 9S0 9 0 5a5 5 0 0 1 5-5z" fill="#f5c400"/></svg></span>
    <span><svg width="6" height="6" viewBox="0 0 12 12"><circle cx="6" cy="6" r="5" fill="none" stroke="#f5c400" stroke-width="1.6"/><path d="M1 6h10M6 1c2 3 2 7 0 10M6 1c-2 3-2 7 0 10" stroke="#f5c400" fill="none"/></svg></span>
  </div>
</div>

<header class="header">
  <div class="brand">
    <span class="brand-mark"></span>
    <span class="brand-name">HALDEN &amp; SONS CONSTRUCTION INC</span>
  </div>
  <div class="contact hotline">
    <svg width="18" height="18" viewBox="0 0 24 24"><path d="M5 3l4 1 1 5-2 2c1 3 3 5 6 6l2-2 5 1 1 4-3 2C10 21 3 14 3 6z" fill="none" stroke="#f5c400" stroke-width="1.8"/></svg>
    <div><b>hotline</b><small>5550142808</small></div>
  </div>
  <div class="contact hours">
    <svg width="18" height="18" viewBox="0 0 24 24"><circle cx="12" cy="12" r="9" fill="none" stroke="#f5c400" stroke-width="1.8"/><path d="M12 7v5l3 3" fill="none" stroke="#f5c400" stroke-width="1.8"/></svg>
    <div><b>Opening Times</b><small>24 / 7 daily</small></div>
  </div>
</header>

<nav class="nav">
  <ul>
    <li class="current" style="left:0">Home</li>
    <li class="sep" style="left:30px"></li>
    <li style="left:38px">Services</li>
    <li class="sep" style="left:78px"></li>
    <li style="left:87px">about us</li>
    <li class="sep" style="left:127px"></li>
    <li style="left:136px">Contact</li>
  </ul>
</nav>

<main>
  <section class="service" style="left:315px;top:112px"><h2>Dormers/Extensions</h2>
    <div class="photo" role="img" aria-label="House dormer extension under construction with scaffolding" style="top:29px;width:122px;height:106px;background:linear-gradient(180deg,#d5d7da 0%,#b9b2ab 35%,#7b4a3c 70%,#5a3a30 100%)"></div></section>
  <section class="service" style="left:465px;top:112px"><h2>Kitchens</h2>
    <div class="photo" role="img" aria-label="White kitchen with island and stainless appliances" style="top:29px;width:130px;height:76px;background:linear-gradient(180deg,#f0efec 0%,#d8d5d0 55%,#8a6446 100%)"></div></section>
  <section class="service" style="left:615px;top:112px"><h2>Masonry/Concrete/Pavers</h2>
    <div class="photo" role="img" aria-label="Asphalt driveway leading to a brick home" style="top:29px;width:130px;height:104px;background:linear-gradient(180deg,#7d8d66 0%,#5f7049 40%,#3b3c40 65%,#3b3c40 85%,#b8b8b6 100%)"></div></section>
  <section class="service" style="left:765px;top:112px"><h2>Pool designs</h2>
    <div class="photo" role="img" aria-label="Backyard pool with paver patio" style="top:29px;width:130px;height:73px;background:linear-gradient(180deg,#6f7a5c 0%,#3aa8c9 40%,#2f96bb 65%,#b48a70 100%)"></div></section>

  <section class="service" style="left:465px;top:247px"><h2>Cultured Stone Veneer</h2>
    <div class="photo" role="img" aria-label="Stone veneer wall beside concrete steps" style="top:29px;width:130px;height:86px;background:linear-gradient(180deg,#7a7f6a 0%,#a0968a 35%,#8c8780 100%)"></div></section>
  <section class="service" style="left:765px;top:244px"><h2>Outdoor Kitchens</h2>
    <div class="photo" role="img" aria-label="Covered outdoor kitchen with seating" style="top:29px;width:130px;height:97px;background:linear-gradient(180deg,#6d5443 0%,#8f939a 40%,#7c7b78 100%)"></div></section>
  <section class="service" style="left:615px;top:275px"><h2>Outdoor Bathrooms</h2>
    <div class="photo" role="img" aria-label="Open-air bathroom with stone basin and shower" style="top:30px;width:130px;height:194px;background:linear-gradient(180deg,#95a774 0%,#dcd9cf 40%,#9a8c7c 70%,#4e3d30 100%)"></div></section>
  <section class="service" style="left:315px;top:278px"><h2>Basement Remodel</h2>
    <div class="photo" role="img" aria-label="Finished basement with dark floor and white cabinets" style="top:29px;width:130px;height:97px;background:linear-gradient(180deg,#9a9793 0%,#6c655f 55%,#463f39 100%)"></div></section>
  <section class="service" style="left:465px;top:393px"><h2>Bathrooms</h2>
    <div class="photo" role="img" aria-label="Grey tiled bathroom with sink and tub" style="top:29px;width:130px;height:96px;background:linear-gradient(180deg,#9d9c98 0%,#8a8985 45%,#dedcd7 100%)"></div></section>
  <section class="service" style="left:315px;top:434px"><h2>Tile work</h2>
    <div class="photo" role="img" aria-label="Tiler removing old wall tiles" style="top:29px;width:130px;height:73px;background:linear-gradient(180deg,#cfc3ae 0%,#a7aaa9 55%,#8d7358 100%)"></div></section>
</main>

<footer class="footer">
  <p>2023 © Halden &amp; Sons Construction - All Rights Reserved</p>
  <div class="social">
    <span><svg width="11" height="8" viewBox="0 0 14 10"><rect width="14" height="10" fill="#a9a8b0"/><path d="M0 0l7 6 7-6" stroke="#2b2a33" fill="none"/></svg></span>
    <span><svg width="9" height="9" viewBox="0 0 12 12"><path d="M3 1l3 1 .5 3-1.5 1c.7 1.6 1.6 2.5 3 3l1-1.5 3 .5 .5 3-2 1C5 11 1 7 1 3z" fill="#a9a8b0"/></svg></span>
    <span><svg width="7" height="10" viewBox="0 0 10 14"><path d="M5 0a5 5 0 0 1 5 5c0 4-5 9-5 9S0 9 0 5a5 5 0 0 1 5-5z" fill="#a9a8b0"/><circle cx="5" cy="5" r="2" fill="#2b2a33"/></svg></span>
    <span><svg width="10" height="10" viewBox="0 0 12 12"><circle cx="6" cy="6" r="5" fill="none" stroke="#a9a8b0" stroke-width="1.4"/><path d="M1 6h10M6 1c2 3 2 7 0 10M6 1c-2 3-2 7 0 10" stroke="#a9a8b0" fill="none"/></svg></span>
  </div>
</footer>
<div class="to-top"><svg width="6" height="4" viewBox="0 0 10 6"><path d="M1 5l4-4 4 4" stroke="#2b2a33" stroke-width="1.6" fill="none"/></svg></div>
</body>
</html>
```